Business Card for Fashion House

We need a business card design for our personalize fashion service for our customers. the business card should reflect reliability, luxury and creativity.
The brand Vastrelle is extracted from "Vibrant Estrella"; Vastrelle provides fashion designs sprinkled with luxury and style tailored for our elite clients character profile.
Vastrelle is created for those who embody class and elegance with a passion for style.
Target Market(s)
Affluent Customers
Industry/Entity Type
Fashion
Contact Information for Business Card
Noura Al Hashimi
Fashion Designer
Telephone: +971 5550192
Mobile +971 555073
Emal q@k.example
Website www.vastrelle.example
Social Media Youtube g+ Facebook Instagram Pin /vastrelle
Font styles to use
Other font styles liked:
- Audrey provided
Look and feel
Each slider illustrates characteristics of the customer's brand and the style your logo design should communicate.

```html
<!DOCTYPE html>
<html lang="en">
<head>
<meta charset="utf-8">
<title>Vastrelle — Business Card</title>
<link href="https://fonts.googleapis.com/css2?family=Cormorant+Garamond:wght@500&family=Roboto:wght@300;400&display=swap" rel="stylesheet">
<style>
  :root {
    --backdrop: #8b8b8b;
    --caption: #6f6f6f;
    --card: #262626;
    --silver: #d9d9d9;
    --ink-light: #e6e6e6;
    --ink-soft: #bdbdbd;
    --rule: #9a9a9a;
  }
  * { margin: 0; padding: 0; box-sizing: border-box; }
  html, body {
    width: 1200px;
    height: 781px;
    overflow: hidden;
    background: var(--backdrop);
  }
  .stage {
    position: relative;
    width: 1200px;
    height: 781px;
  }
  .finish-caption {
    position: absolute;
    top: 49px;
    left: 0;
    width: 1200px;
    text-align: center;
    font: 300 10px "Roboto", sans-serif;
    color: var(--caption);
  }
  .card {
    position: absolute;
    left: 358px;
    width: 454px;
    height: 251px;
    background: var(--card);
  }
  .card--front { top: 103px; }
  .card--back { top: 410px; }

  .brand {
    position: absolute;
    display: flex;
    flex-direction: column;
    align-items: center;
    transform: translateX(-50%);
  }
  .brand-dot {
    border: 1.5px solid var(--silver);
    border-radius: 50%;
  }
  .brand-name {
    font-family: "Cormorant Garamond", serif;
    font-weight: 500;
    color: var(--silver);
    text-transform: uppercase;
    white-space: nowrap;
  }
  .card--front .brand { left: 227px; top: 74px; }
  .card--front .brand-dot { width: 42px; height: 42px; margin-bottom: 32px; }
  .card--front .brand-name { font-size: 22px; letter-spacing: 0.42em; margin-right: -0.42em; }

  .card--back .brand { left: 343px; top: 140px; }
  .card--back .brand-dot { width: 34px; height: 34px; margin-bottom: 23px; }
  .card--back .brand-name { font-size: 16px; letter-spacing: 0.38em; margin-right: -0.38em; }

  .holder {
    position: absolute;
    left: 43px;
    top: 45px;
    font-family: "Roboto", sans-serif;
  }
  .holder-name { font-size: 14.5px; font-weight: 400; color: var(--ink-light); }
  .holder-role { font-size: 10.5px; font-weight: 300; color: var(--ink-soft); margin-top: 1px; }

  .contacts {
    position: absolute;
    left: 43px;
    top: 192px;
    display: flex;
    font: 300 10.5px/14.5px "Roboto", sans-serif;
    color: var(--ink-soft);
  }
  .contacts-phones { padding-right: 10px; }
  .contacts-web {
    padding-left: 10px;
    border-left: 1px solid var(--rule);
  }
</style>
</head>
<body>
<main class="stage">
  <p class="finish-caption">Embossing&nbsp; + foil stamping</p>

  <section class="card card--front" aria-label="Card front">
    <div class="brand">
      <span class="brand-dot"></span>
      <span class="brand-name">Vastrelle</span>
    </div>
  </section>

  <section class="card card--back" aria-label="Card back">
    <div class="holder">
      <p class="holder-name">Noura Al Hashimi</p>
      <p class="holder-role">Fashion Designer</p>
    </div>
    <div class="contacts">
      <div class="contacts-phones">
        <p>T: +971 5550192</p>
        <p>M +971 555073</p>
      </div>
      <div class="contacts-web">
        <p>q@k.example</p>
        <p>www.vastrelle.example</p>
      </div>
    </div>
    <div class="brand">
      <span class="brand-dot"></span>
      <span class="brand-name">Vastrelle</span>
    </div>
  </section>
</main>
</body>
</html>
```